Stationary package for Health Care company

COMPANY NAME: Corvanta.
We have a company logo. We need to create a stationary package for a new health care company. The package needs to be unique, high tech, innovative (perhaps a folded business card, or something with a die-cut). It needs to be memorable.

The company makes in-home allergy test kits - customer takes an allergy test at home (with special medical device found in the kit) then, they send in their blood samples, and the company sends back a detailed report of what they are/are not allergic to.

We need:
business cards
thank you cards
labels
stationary
envelope
9" x 12" Pocket folder

Corvanta (The company) has a brochure for the product (called Bluvaris). The stationary package should compliment the brochure. The brochure will reside in the pocket folder and they must look good together. Brochure uploaded. Note: the brochure is flat. Once folded - all you will actually see in the pocket folder is the cover with the man with outstretched arms.

INFO TO BE USED ON STATIONARY: DO NOT TRY AND CONTACT THIS PERSON!

Martin R. Hollaway
Chief Executive Officer
48 Kestrel Meadow Parkway #210
Brookhaven IL 60412
Phone: 847-555-0182
Web site: www.corvanta-example.com
email: mhollaway@corvanta-example.com

I have added all of the information to be used on the stationary package. PLEASE DO NOT TRY TO CONTACT THIS PERSON OR COMPANY. If you have any questions - contact me. Thank you. Glen

I've uploaded a cleaned up version of the Corvanta logo as a 300 dpi PSD if anyone needs it. Thank you. Glen

Target Market(s)

Doctors, hospitals, laboratories.

Industry/Entity Type

Medical

Requirements
Must have
• Must be memorable, high-tech. Must work together with Bluvaris brochure. Descriptive words: freedom, breathe, clean, fresh

```html
<!DOCTYPE html>
<html lang="en">
<head>
<meta charset="utf-8">
<title>Corvanta Business Card</title>
<link rel="stylesheet" href="https://fonts.googleapis.com/css2?family=Questrial&family=Raleway:wght@700&display=swap">
<style>
  :root {
    --bg: #e6e5ea;
    --card-white: #f6f7fa;
    --navy: #2a3590;
    --royal: #4b5cb4;
    --royal-light: #5d6fc2;
    --sky: #c7d3ea;
    --ink: #3a3d4a;
    --tagline: #a9c4f2;
  }
  * { margin: 0; padding: 0; box-sizing: border-box; }
  html, body {
    width: 1200px; height: 934px; overflow: hidden;
    background: var(--bg);
    font-family: "Questrial", sans-serif;
  }
  .canvas { position: relative; width: 1200px; height: 934px; }

  .card {
    position: absolute;
    width: 665px; height: 380px;
    box-shadow: 0 6px 18px rgba(40, 45, 80, 0.18);
    overflow: hidden;
  }

  /* Card back */
  .card-back {
    left: 110px; top: 60px;
    background: linear-gradient(160deg, var(--royal-light) 0%, var(--navy) 100%);
    display: flex; flex-direction: column; align-items: center; justify-content: center;
  }
  .card-back .wordmark { color: #ffffff; font-size: 66px; letter-spacing: 1px; line-height: 1; }
  .card-back .tagline { color: var(--tagline); font-size: 17px; margin-top: 14px; letter-spacing: 0.4px; }

  /* Card front */
  .card-front { left: 425px; top: 494px; background: var(--card-white); }
  .card-front .wordmark {
    position: absolute; left: 56px; top: 78px;
    color: var(--royal); font-size: 54px; line-height: 1;
  }
  .person { position: absolute; right: 52px; top: 40px; text-align: right; }
  .person .name {
    font-family: "Raleway", sans-serif; font-weight: 700;
    color: var(--royal); font-size: 17px; letter-spacing: 0.6px; text-transform: uppercase;
  }
  .person .role { color: var(--ink); font-size: 14px; margin-top: 4px; }

  .address {
    position: absolute; left: 56px; top: 180px;
    color: var(--ink); font-size: 13px; line-height: 19px; font-style: normal;
  }
  .contacts { position: absolute; left: 56px; top: 232px; list-style: none; }
  .contacts li {
    display: flex; align-items: center; gap: 12px;
    color: var(--ink); font-size: 13px; height: 21px;
  }
  .contacts .icon {
    width: 15px; height: 15px; border-radius: 3px; background: var(--royal);
    display: flex; align-items: center; justify-content: center;
  }
  .contacts .icon svg { width: 11px; height: 11px; }

  .wave { position: absolute; left: 0; top: 0; width: 665px; height: 380px; }
</style>
</head>
<body>
<main class="canvas">

  <section class="card card-back" aria-label="Business card back">
    <div class="wordmark">Corvanta</div>
    <div class="tagline">Clear Answers For Easier Breathing</div>
  </section>

  <section class="card card-front" aria-label="Business card front">
    <svg class="wave" viewBox="0 0 665 380" aria-hidden="true">
      <path d="M0 380 L0 362 C170 352 380 290 665 172 L665 380 Z" fill="var(--sky)"/>
      <path d="M0 380 L0 372 C200 362 420 300 665 198 L665 380 Z" fill="var(--royal)"/>
      <path d="M170 380 C330 350 490 300 665 236 L665 380 Z" fill="var(--navy)" opacity="0.55"/>
      <path d="M0 356 C180 346 390 282 665 160" fill="none" stroke="var(--navy)" stroke-width="2"/>
    </svg>

    <div class="wordmark">Corvanta</div>

    <div class="person">
      <div class="name">Martin R. Hollaway</div>
      <div class="role">Chief Executive Officer</div>
    </div>

    <address class="address">
      48 Kestrel Meadow Parkway #210<br>
      Brookhaven IL 60412
    </address>

    <ul class="contacts">
      <li>
        <span class="icon"><svg viewBox="0 0 12 12"><path d="M3 1.5 L4.6 3.6 L3.8 4.6 C4.4 6 5.8 7.4 7.3 8.1 L8.3 7.3 L10.5 8.9 L9.6 10.5 C5.6 10.3 1.7 6.4 1.5 2.4 Z" fill="#fff"/></svg></span>
        847-555-0182
      </li>
      <li>
        <span class="icon"><svg viewBox="0 0 12 12"><rect x="1.5" y="3" width="9" height="6.5" fill="none" stroke="#fff" stroke-width="1.2"/><path d="M1.5 3 L6 6.8 L10.5 3" fill="none" stroke="#fff" stroke-width="1.2"/></svg></span>
        info@corvanta-example.com
      </li>
      <li>
        <span class="icon"><svg viewBox="0 0 12 12"><circle cx="6" cy="6" r="4.4" fill="none" stroke="#fff" stroke-width="1.1"/><ellipse cx="6" cy="6" rx="1.9" ry="4.4" fill="none" stroke="#fff" stroke-width="1"/><path d="M1.6 6 H10.4" stroke="#fff" stroke-width="1"/></svg></span>
        www.corvanta-example.com
      </li>
    </ul>
  </section>

</main>
</body>
</html>
```